Pool Builder Website Design in arizona

Our current site is located here: tidemoor.net

We are looking to give this a modern facelift. We will be cutting your design into a wordpress theme so we can utilize the CMS plateform backend.

Look and Feel
• Clean cut and professional
• Mobile friendly
• Updated from old site
• Feel intrigued but relax (do you have trust logos? Odile looking into this)
Colors
• Warm tropical neutral colors
• Orange, brown, blues
- Please make the site modern and more sleek look that looks like a 2015 style design and NOT 1999.
- Must be coded as a wordpress theme
- must create a home page, inner page and blog page
- must allow client to BLOG using the post section in wordpress

This pool company is a pool builder/installer in Phoenix arizona.

NOTE::: Please create a home page and one internal page.

Industry/Entity Type

Builder

Coding

Coded - Design and coding required

Number of Pages Required

3 page

Font styles to use
Serif
Sans Serif

Requirements
Must have
• - Must be coded as a wordpress theme
• - must create a home page, inner page and blog page
• - must allow client to BLOG using the post section in wordpress

```html
<!DOCTYPE html>
<html lang="en">
<head>
<meta charset="utf-8">
<title>Tidemoor Pools – Fiberglass Pool Experts</title>
<link rel="stylesheet" href="https://fonts.googleapis.com/css2?family=Dosis:wght@400;500;600;700&family=Lato:wght@300;700&family=Pathway+Gothic+One&display=swap">
<style>
:root{
  --ink:#0a0405;
  --white:#ffffff;
  --teal:#1fa3c6;
  --orange:#f7a11a;
  --text:#5a5a5a;
  --dark:#1c2123;
  --sky:#3f93c4;
  --sky-deep:#1d6a9c;
}
*{box-sizing:border-box;margin:0;padding:0}
html,body{width:1200px;height:1118px;overflow:hidden;background:var(--white)}
body{position:relative;font-family:'Lato',sans-serif}
.topbar{position:absolute;left:0;top:0;width:1200px;height:31px;background:var(--ink);color:var(--white);font:600 10px 'Dosis',sans-serif;}
.topbar .contacts{position:absolute;left:92px;top:9px;display:flex;gap:6px;align-items:center}
.topbar .contacts svg{width:9px;height:9px;fill:var(--white);margin-right:3px;vertical-align:-1px}
.topbar .social{position:absolute;right:94px;top:10px;display:flex;gap:22px}
.topbar .social span{width:10px;height:10px;border-radius:50%;background:var(--white)}
.header{position:absolute;left:0;top:31px;width:1200px;height:106px;background:var(--white)}
.brand{position:absolute;left:89px;top:35px;display:flex;align-items:center;gap:8px;font:700 27px 'Dosis',sans-serif;color:var(--sky-deep)}
.brand i{width:22px;height:22px;border-radius:50%;background:var(--teal);display:block}
.nav{position:absolute;left:786px;top:58px;display:flex;gap:26px;font:500 11px 'Dosis',sans-serif;color:var(--teal);letter-spacing:.2px}
.nav svg{width:12px;height:9px;stroke:var(--teal);fill:none;margin-right:6px;vertical-align:-1px}
.hero{position:absolute;left:0;top:137px;width:1200px;height:397px;background:radial-gradient(ellipse at 55% 55%,#9fd0ea 0%,#4da3d3 35%,#2a7fb6 75%,#1d5f8f 100%)}
.welcome{position:absolute;left:89px;top:147px;width:322px;height:193px;background:rgba(255,255,255,.82);padding:30px 28px;font:400 31px/35px 'Dosis',sans-serif;color:var(--ink)}
.welcome b{font-weight:700}
.intro{position:absolute;left:89px;top:577px;width:760px;font:300 15px/16.5px 'Lato',sans-serif;color:var(--text)}
.intro b{font-weight:700;color:#333}
.btn{position:absolute;display:flex;align-items:center;justify-content:center;gap:10px;background:var(--orange);color:var(--white);font-family:'Dosis',sans-serif;font-weight:500}
.btn svg{fill:none;stroke:var(--white);stroke-width:2}
.btn-about{left:874px;top:581px;width:146px;height:47px;font-size:23px}
.btn-about svg{width:30px;height:30px}
.features{position:absolute;left:0;top:688px;width:1200px;height:369px;background:linear-gradient(180deg,#6a5748 0%,#8a7b6a 25%,#9a958c 55%,#6fb8d6 85%,#4aa3cc 100%)}
.features .band{position:absolute;left:0;top:58px;width:1200px;height:283px;background:rgba(236,236,236,.72)}
.features h2{position:absolute;left:438px;top:134px;font:400 28px 'Dosis',sans-serif;color:#222;white-space:nowrap}
.features p{position:absolute;left:438px;top:180px;width:670px;font:400 15px/17px 'Pathway Gothic One',sans-serif;color:#444}
.btn-install{left:977px;top:271px;width:131px;height:47px;font-size:16px}
.btn-install svg{width:30px;height:30px}
.footer{position:absolute;left:0;top:1057px;width:1200px;height:61px;background:var(--dark)}
.footer svg{position:absolute;left:1098px;top:30px;width:10px;height:10px;fill:var(--white)}
</style>
</head>
<body>
<div class="topbar">
  <div class="contacts">
    <span><svg viewBox="0 0 10 10"><path d="M2 0l2 2-1 1.5c.8 1.5 2 2.7 3.5 3.5L8 6l2 2-1.5 2C4 9.5.5 6 0 1.5z"/></svg>1-800-555-0142 (TOLL FREE)</span><span>|</span>
    <span><svg viewBox="0 0 10 10"><path d="M2 0l2 2-1 1.5c.8 1.5 2 2.7 3.5 3.5L8 6l2 2-1.5 2C4 9.5.5 6 0 1.5z"/></svg>+1 (602) 555-0187</span><span>|</span>
    <span><svg viewBox="0 0 10 10"><path d="M0 1h10v8H0z M0 1l5 4 5-4" /></svg>hello@tidemoor.net</span>
  </div>
  <div class="social"><span></span><span></span><span></span><span></span></div>
</div>
<header class="header">
  <div class="brand"><i></i>Tidemoor Pools</div>
  <nav class="nav">
    <span>STYLES</span><span>PORTFOLIO</span><span>INSTALLATION</span><span>ABOUT US</span>
    <span><svg viewBox="0 0 12 9"><rect x=".5" y=".5" width="11" height="8"/><path d="M.5.5l5.5 4 5.5-4"/></svg>CONTACT</span>
  </nav>
</header>
<section class="hero" role="img" aria-label="Photo of a smiling child splashing in a blue pool">
  <div class="welcome">Welcome to <b>Tidemoor Pools</b><br>the <b>Fiberglass</b> Pool Experts!</div>
</section>
<p class="intro">A <b>Phoenix fiberglass pool</b> is more than just a relaxing piece of heaven, it is an investment. Why spend your money on a pool that requires more maintenance and scratches your feet when you can enjoy the smooth feeling of fiberglass on your toes? Fiberglass pools offer many unique advantages over concrete pools, and Tidemoor Pools are <b>the premier AZ fiberglass pool builders</b>.</p>
<a class="btn btn-about">About us <svg viewBox="0 0 30 30"><circle cx="15" cy="15" r="13"/><path d="M8 15h13M16 10l5 5-5 5"/></svg></a>
<section class="features" role="img" aria-label="Photo of a rock waterfall feature pouring into a pool">
  <div class="band"></div>
  <h2>We also offer many other products and services</h2>
  <p>to enhance your yard and increase the value of your home. Check out some of our cost effective and sensuous fiberglass spools and spas, our beautiful and calming custom water features, or our fun custom beehives, firepits, and barbecues. Our fiberglass pools come in many sizes and styles and installation is a breeze. Call or stop in today to see how we can make your yard "A small bit of paradise"! We are the best arizona pool builder.</p>
  <a class="btn btn-install">Installation <svg viewBox="0 0 30 30"><circle cx="15" cy="15" r="13"/><path d="M8 15h13M16 10l5 5-5 5"/></svg></a>
</section>
<footer class="footer">
  <svg viewBox="0 0 10 10"><path d="M5 1l4 5H6v3H4V6H1z"/></svg>
</footer>
</body>
</html>
```